Technical Refinement & Corporate Adaptation of AI Graphics

We have a follow-up project for you that involves technically refining existing, AI-generated graphics and recreating them professionally in Microsoft PowerPoint. - as you did already. The content and core structure should remain unchanged, but the visual style needs to be aligned with the corporate design of the Kraftwerkhaus Morlen (colors, typography, and visual language). The primary focus is to ensure all elements are fully editable, perfectly aligned, and deliver a clean, scientific-technical look.

```html
<!DOCTYPE html>
<html lang="en">
<head>
<meta charset="utf-8">
<title>Business Models, Governance &amp; Implementation – Layout Options</title>
<link href="https://fonts.googleapis.com/css2?family=Figtree:wght@300;400;500;600;700&display=swap" rel="stylesheet">
<style>
:root{
  --board:#cbcbcb;
  --paper:#ffffff;
  --green:#6b8a06;
  --green-dark:#5f7c00;
  --green-soft:#e3e8da;
  --ink:#111111;
  --text:#5a5a5a;
  --muted:#6d6d6d;
  --rule:#dcdcdc;
  --frame-grey:#8a8a8a;
  --frame-dark:#2f2f2f;
}
*{box-sizing:border-box;margin:0;padding:0}
html,body{width:967px;height:1200px;overflow:hidden}
body{background:var(--board);font-family:"Figtree",Arial,sans-serif;position:relative;color:var(--text)}

.option-label{position:absolute;left:45px;font-size:24px;font-weight:400;color:var(--ink);letter-spacing:.5px}
.option-label--one{top:21px}
.option-label--two{top:598px;left:48px}

.slide{position:absolute;left:42px;width:883px;height:497px;background:var(--paper);box-shadow:0 6px 14px rgba(0,0,0,.25);overflow:hidden}
.slide--one{top:71px}
.slide--two{top:639px}

.accent-bar{position:absolute;top:24px;width:137px;height:7px;background:var(--green-dark)}
.slide-title{position:absolute;top:43px;font-size:18.4px;font-weight:700;color:var(--ink);letter-spacing:.1px;white-space:nowrap}
.slide-subtitle{position:absolute;top:73px;font-size:15px;font-weight:300;color:#444;white-space:nowrap}
.slide--one .accent-bar{left:379px}
.slide--one .slide-title,.slide--one .slide-subtitle{left:0;width:883px;text-align:center;margin-left:-6px}
.slide--two .accent-bar{left:36px;top:23px}
.slide--two .slide-title,.slide--two .slide-subtitle{left:36px}

.brand{position:absolute;top:27px;right:36px;display:flex;align-items:center;gap:6px}
.brand-dot{width:22px;height:22px;border-radius:50%;background:var(--green-soft)}
.brand-name{font-size:13px;font-weight:600;color:var(--green);line-height:14px}

.process-frame{position:absolute;left:35px;top:100px;width:813px;height:193px;border:1.5px solid var(--green);border-radius:6px}
.timeline{position:absolute;left:35px;top:176px;width:813px;height:1.5px;background:var(--rule)}
.edge-marker{position:absolute;border-radius:50%}
.edge-marker--solid{width:9px;height:9px;background:var(--green-dark);margin:-4.5px 0 0 -4.5px}
.edge-marker--ring{width:15px;height:15px;border:3px solid var(--rule);background:#fff;margin:-7.5px 0 0 -7.5px}

.step{position:absolute;left:calc(var(--x) - 65px);top:0;width:130px;height:300px;text-align:center}
.step-icon{position:absolute;left:37px;top:121px;width:56px;height:56px;border-radius:50%;background:var(--green-soft);display:flex;align-items:center;justify-content:center}
.step-icon svg{width:28px;height:28px}
.step-number{position:absolute;left:55.5px;top:168px;width:19px;height:19px;border-radius:50%;background:#fff;border:1px solid var(--green);font-size:8px;font-weight:700;color:var(--ink);line-height:17px}
.step-title{position:absolute;left:0;top:194px;width:130px;font-size:13.4px;font-weight:500;color:var(--green);line-height:19px}
.step-text{position:absolute;left:18px;top:236px;width:94px;font-size:10px;font-weight:300;color:var(--text);line-height:14px}

.panel{position:absolute;top:305px;height:132px;border-radius:4px;background:transparent}
.panel--methods{left:35px;width:407px;border:1px solid var(--frame-grey)}
.panel--benefits{left:449px;width:397px;border:1px solid var(--frame-dark)}
.panel-icon{position:absolute;left:50%;top:8px;width:32px;height:32px;margin-left:-16px}
.panel-heading{position:absolute;left:0;top:44px;width:100%;display:flex;align-items:center;justify-content:center;gap:10px;font-size:13.4px;font-weight:500}
.panel-heading::before,.panel-heading::after{content:"";display:block;height:1px;width:92px;background:var(--rule)}
.panel--methods .panel-heading{color:var(--muted)}
.panel--benefits .panel-heading{color:var(--ink)}
.panel-item{position:absolute;top:67px;left:calc(var(--x) - 36px);width:72px;text-align:center;font-size:10px;font-weight:300;color:var(--text);line-height:14px}
.panel-item::before{content:"";display:block;width:13px;height:13px;margin:0 auto 10px;border-radius:50%;background:var(--green-dark);box-shadow:0 0 0 3px var(--green-soft)}
.panel-item--wide{left:calc(var(--x) - 46px);width:92px}
.panel--benefits .panel-item{left:calc(var(--x) - 33px);width:66px}
.panel--benefits .panel-item::before{margin-bottom:4px}

.footer-line{position:absolute;top:470px;height:1px;background:var(--green)}
.footer-line--left{left:135px;width:55px}
.footer-line--right{left:693px;width:56px}
.footer-dot{position:absolute;top:467.5px;width:6px;height:6px;border-radius:50%;background:var(--green-dark)}
.footer-globe{position:absolute;left:201px;top:460px;width:22px;height:22px}
.footer-tagline{position:absolute;left:231px;top:463px;font-size:10.3px;font-weight:400;color:var(--green);white-space:nowrap}
.page-number{position:absolute;left:809px;top:457px;width:40px;height:40px;background:var(--green);color:#fff;font-size:17px;font-weight:300;text-align:center;line-height:40px}

.network-backdrop{position:absolute;left:599px;top:207px;width:284px;height:290px;background:radial-gradient(ellipse at 60% 55%,rgba(225,225,225,.55),rgba(240,240,240,.25) 55%,rgba(255,255,255,0) 75%)}
</style>
</head>
<body>

<svg width="0" height="0" style="position:absolute" aria-hidden="true">
  <defs>
    <symbol id="icon-plant" viewBox="0 0 28 28"><g fill="none" stroke="#5f7c00" stroke-width="1.6" stroke-linecap="round" stroke-linejoin="round"><path d="M4 15h20a10 8 0 0 1-20 0z"/><path d="M14 15V6"/><path d="M14 10c-3-1-5-3-5-5 3 0 5 2 5 5zM14 9c2-2 4-3 6-2-1 2-3 3-6 2z"/><path d="M9 15v-4M19 15v-3"/></g></symbol>
    <symbol id="icon-link" viewBox="0 0 28 28"><g fill="none" stroke="#5f7c00" stroke-width="2.2" stroke-linecap="round"><path d="M12 16l-3 3a3.5 3.5 0 0 1-5-5l4-4a3.5 3.5 0 0 1 5 0"/><path d="M16 12l3-3a3.5 3.5 0 0 1 5 5l-4 4a3.5 3.5 0 0 1-5 0"/><path d="M11 17l6-6"/></g></symbol>
    <symbol id="icon-finance" viewBox="0 0 28 28"><g fill="none" stroke="#5f7c00" stroke-width="1.5" stroke-linecap="round" stroke-linejoin="round"><ellipse cx="9" cy="21" rx="5" ry="2"/><path d="M4 17v4M14 17v4"/><ellipse cx="9" cy="17" rx="5" ry="2"/><path d="M4 13v4M14 13v4"/><ellipse cx="9" cy="13" rx="5" ry="2"/><path d="M6 8l5-3 4 2 6-4M18 3h3v3"/></g><circle cx="19" cy="18" r="5.5" fill="#5f7c00"/><text x="19" y="21.5" font-size="9" font-family="Arial" font-weight="700" fill="#fff" text-anchor="middle">$</text></symbol>
    <symbol id="icon-gavel" viewBox="0 0 28 28"><g fill="none" stroke="#5f7c00" stroke-width="1.6" stroke-linecap="round" stroke-linejoin="round"><path d="M8 9l5-5 5 5-5 5z"/><path d="M15 12l9 9"/><path d="M4 22h11M5 25h9"/></g></symbol>
    <symbol id="icon-ideas" viewBox="0 0 28 28"><g fill="none" stroke="#5f7c00" stroke-width="1.5" stroke-linecap="round" stroke-linejoin="round"><path d="M9 19v-2a6 6 0 1 1 4 0v2z"/><path d="M9 22h4"/><circle cx="21" cy="8" r="3"/><path d="M21 3v2M21 11v2M16 8h2M24 8h2M17.5 4.5l1.4 1.4M23.1 10.1l1.4 1.4M17.5 11.5l1.4-1.4M23.1 5.9l1.4-1.4"/><path d="M18 17c2 0 4-1 4-3"/></g></symbol>
    <symbol id="icon-board" viewBox="0 0 28 28"><g fill="none" stroke="#5f7c00" stroke-width="1.6" stroke-linecap="round" stroke-linejoin="round"><path d="M3 4h22M5 4v14h18V4"/><path d="M14 18v4M11 25l3-3 3 3"/><path d="M9 15v-3M12 15v-5M15 15v-4M18 15V8M8 15h12"/></g></symbol>
    <symbol id="icon-tools" viewBox="0 0 32 32"><g fill="none" stroke="#5f7c00" stroke-width="1.6" stroke-linecap="round" stroke-linejoin="round"><path d="M14 2h4l1 4 3 1.5 3.5-2 3 3-2 3.5L28 15l4 1v0l-4 1-1 3 2 3.5-3 3-3.5-2L19 26l-1 4h-4l-1-4-3-1.5-3.5 2-3-3 2-3.5L4 17l-4-1 4-1 1-3-2-3.5 3-3 3.5 2L13 6z" transform="scale(.94) translate(1 1)"/><circle cx="15" cy="15" r="6"/><path d="M19.5 19.5l6 6"/></g></symbol>
    <symbol id="icon-benefit" viewBox="0 0 32 32"><g fill="none" stroke="#5f7c00" stroke-width="1.6" stroke-linecap="round" stroke-linejoin="round"><path d="M3 24l5-5c2-2 4-2 6-1h5a2 2 0 0 1 0 4h-5"/><path d="M14 22h6l7-6a2 2 0 0 1 3 3l-8 8H10l-3 3"/><path d="M20 3l1.5 3 3.3.5-2.4 2.3.6 3.3-3-1.6-3 1.6.6-3.3-2.4-2.3 3.3-.5z"/><path d="M9 9l.8 1.6 1.7.3-1.2 1.2.3 1.7-1.6-.8-1.6.8.3-1.7-1.2-1.2 1.7-.3zM28 9v3M26.5 10.5h3"/></g></symbol>
    <symbol id="icon-globe" viewBox="0 0 22 22"><g fill="none" stroke="#6b8a06" stroke-width="1"><circle cx="11" cy="11" r="10.5"/><circle cx="11" cy="11" r="6"/><ellipse cx="11" cy="11" rx="2.6" ry="6"/><path d="M5 11h12M6 8h10M6 14h10"/></g></symbol>
  </defs>
</svg>

<h2 class="option-label option-label--one">OPTION # 01</h2>

<section class="slide slide--one">
  <div class="accent-bar"></div>
  <h1 class="slide-title">BUSINESS MODELS, GOVERNANCE &amp; IMPLEMENTATION</h1>
  <p class="slide-subtitle">From concepts to successful and scalable implementation</p>
  <div class="brand"><span class="brand-dot"></span><span class="brand-name">Kraftwerkhaus<br>Morlen</span></div>

  <div class="process-frame"></div>
  <div class="timeline"></div>
  <span class="edge-marker edge-marker--solid" style="left:35px;top:179px"></span>
  <span class="edge-marker edge-marker--ring" style="left:35px;top:197px"></span>
  <span class="edge-marker edge-marker--solid" style="left:35px;top:214px"></span>
  <span class="edge-marker edge-marker--solid" style="left:848px;top:179px"></span>
  <span class="edge-marker edge-marker--ring" style="left:848px;top:197px"></span>
  <span class="edge-marker edge-marker--solid" style="left:848px;top:214px"></span>

  <div class="step" style="--x:107px"><div class="step-icon"><svg><use href="#icon-plant"/></svg></div><span class="step-number">01</span><h3 class="step-title">Stakeholders &amp;Ecosystem</h3><p class="step-text">Actors, roles, partnerships , public acceptance</p></div>
  <div class="step" style="--x:232px"><div class="step-icon"><svg><use href="#icon-link"/></svg></div><span class="step-number">02</span><h3 class="step-title">Value Proposition&amp; Value Chains</h3><p class="step-text">Customer needs ,services ,resources ,value flows</p></div>
  <div class="step" style="--x:365px"><div class="step-icon"><svg><use href="#icon-finance"/></svg></div><span class="step-number">03</span><h3 class="step-title">Business Model Design</h3><p class="step-text">Revenues, costs , risks, key resources</p></div>
  <div class="step" style="--x:503px"><div class="step-icon"><svg><use href="#icon-gavel"/></svg></div><span class="step-number">04</span><h3 class="step-title">Market &amp; Regulatory Framework</h3><p class="step-text">Policies, incentives , market rules , permits</p></div>
  <div class="step" style="--x:639px"><div class="step-icon"><svg><use href="#icon-ideas"/></svg></div><span class="step-number">05</span><h3 class="step-title">Implementation Pathways</h3><p class="step-text">Pilots, scaling , financing, roll-out strategies</p></div>
  <div class="step" style="--x:776px"><div class="step-icon"><svg><use href="#icon-board"/></svg></div><span class="step-number">06</span><h3 class="step-title">Monitoring &amp; Adaptation</h3><p class="step-text">KPIs, learning , adaptation and improvement</p></div>

  <div class="panel panel--methods">
    <svg class="panel-icon"><use href="#icon-tools"/></svg>
    <h3 class="panel-heading">Methods &amp; Tools</h3>
    <p class="panel-item" style="--x:57px">Stakeholder analysis</p>
    <p class="panel-item" style="--x:130px">Business model canvas</p>
    <p class="panel-item panel-item--wide" style="--x:208px">Financial &amp; economic analysis</p>
    <p class="panel-item" style="--x:286px">Governance &amp; policy analysis</p>
    <p class="panel-item" style="--x:363px">MCDA</p>
  </div>
  <div class="panel panel--benefits">
    <svg class="panel-icon"><use href="#icon-benefit"/></svg>
    <h3 class="panel-heading">Benefits &amp; Results</h3>
    <p class="panel-item" style="--x:46px">Bankable and viable solutions</p>
    <p class="panel-item" style="--x:124px">Clear value for all stakeholders</p>
    <p class="panel-item" style="--x:202px">Reduced risks and barriers</p>
    <p class="panel-item" style="--x:279px">Faster and smoother implementation</p>
    <p class="panel-item" style="--x:357px">Long-term success and scalability</p>
  </div>

  <span class="footer-dot" style="left:132px"></span>
  <span class="footer-line footer-line--left"></span>
  <svg class="footer-globe"><use href="#icon-globe"/></svg>
  <p class="footer-tagline">Holistic research, analysis and solutions for a secure, climate-neutral and resource-efficient future</p>
  <span class="footer-line footer-line--right"></span>
  <span class="footer-dot" style="left:746px"></span>
  <div class="page-number">01</div>
</section>

<h2 class="option-label option-label--two">OPTION # 02</h2>

<section class="slide slide--two">
  <div class="network-backdrop" role="img" aria-label="Faint network of connected nodes in the background"></div>
  <div class="accent-bar"></div>
  <h1 class="slide-title">BUSINESS MODELS, GOVERNANCE &amp; IMPLEMENTATION</h1>
  <p class="slide-subtitle">From concepts to successful and scalable implementation</p>
  <div class="brand"><span class="brand-dot"></span><span class="brand-name">Kraftwerkhaus<br>Morlen</span></div>

  <div class="process-frame"></div>
  <div class="timeline"></div>
  <span class="edge-marker edge-marker--solid" style="left:35px;top:179px"></span>
  <span class="edge-marker edge-marker--ring" style="left:35px;top:197px"></span>
  <span class="edge-marker edge-marker--solid" style="left:35px;top:214px"></span>
  <span class="edge-marker edge-marker--solid" style="left:848px;top:179px"></span>
  <span class="edge-marker edge-marker--ring" style="left:848px;top:197px"></span>
  <span class="edge-marker edge-marker--solid" style="left:848px;top:214px"></span>

  <div class="step" style="--x:107px"><div class="step-icon"><svg><use href="#icon-plant"/></svg></div><span class="step-number">01</span><h3 class="step-title">Stakeholders &amp;Ecosystem</h3><p class="step-text">Actors, roles, partnerships , public acceptance</p></div>
  <div class="step" style="--x:232px"><div class="step-icon"><svg><use href="#icon-link"/></svg></div><span class="step-number">02</span><h3 class="step-title">Value Proposition&amp; Value Chains</h3><p class="step-text">Customer needs ,services ,resources ,value flows</p></div>
  <div class="step" style="--x:365px"><div class="step-icon"><svg><use href="#icon-finance"/></svg></div><span class="step-number">03</span><h3 class="step-title">Business Model Design</h3><p class="step-text">Revenues, costs , risks, key resources</p></div>
  <div class="step" style="--x:503px"><div class="step-icon"><svg><use href="#icon-gavel"/></svg></div><span class="step-number">04</span><h3 class="step-title">Market &amp; Regulatory Framework</h3><p class="step-text">Policies, incentives , market rules , permits</p></div>
  <div class="step" style="--x:639px"><div class="step-icon"><svg><use href="#icon-ideas"/></svg></div><span class="step-number">05</span><h3 class="step-title">Implementation Pathways</h3><p class="step-text">Pilots, scaling , financing, roll-out strategies</p></div>
  <div class="step" style="--x:776px"><div class="step-icon"><svg><use href="#icon-board"/></svg></div><span class="step-number">06</span><h3 class="step-title">Monitoring &amp; Adaptation</h3><p class="step-text">KPIs, learning , adaptation and improvement</p></div>

  <div class="panel panel--methods">
    <svg class="panel-icon"><use href="#icon-tools"/></svg>
    <h3 class="panel-heading">Methods &amp; Tools</h3>
    <p class="panel-item" style="--x:57px">Stakeholder analysis</p>
    <p class="panel-item" style="--x:130px">Business model canvas</p>
    <p class="panel-item panel-item--wide" style="--x:208px">Financial &amp; economic analysis</p>
    <p class="panel-item" style="--x:286px">Governance &amp; policy analysis</p>
    <p class="panel-item" style="--x:363px">MCDA</p>
  </div>
  <div class="panel panel--benefits">
    <svg class="panel-icon"><use href="#icon-benefit"/></svg>
    <h3 class="panel-heading">Benefits &amp; Results</h3>
    <p class="panel-item" style="--x:46px">Bankable and viable solutions</p>
    <p class="panel-item" style="--x:124px">Clear value for all stakeholders</p>
    <p class="panel-item" style="--x:202px">Reduced risks and barriers</p>
    <p class="panel-item" style="--x:279px">Faster and smoother implementation</p>
    <p class="panel-item" style="--x:357px">Long-term success and scalability</p>
  </div>

  <span class="footer-dot" style="left:132px"></span>
  <span class="footer-line footer-line--left"></span>
  <svg class="footer-globe"><use href="#icon-globe"/></svg>
  <p class="footer-tagline">Holistic research, analysis and solutions for a secure, climate-neutral and resource-efficient future</p>
  <span class="footer-line footer-line--right"></span>
  <span class="footer-dot" style="left:746px"></span>
  <div class="page-number">02</div>
</section>

</body>
</html>
```